Life Coach for Lawyers Business Card Design

Elegant, original, business card design for life coaching service for associate attorneys who work in big law and struggle with stress, overwhelm, and time management. Double sided design.

Target Market(s)

Women associate attorneys who work in big law and struggle with stress, overwhelm, and time management.

Industry/Entity Type

Life Coaching

Contact Information for Business Card

Marissa Pendrell
Life Coach
518.677.3941
calmbriefcounsel.net
marissa@calmbriefcounsel.net
@calmbriefcounsel (Instagram)

Font styles to use
Other font styles liked:
• Silver South font duo. See uploaded files.

Requirements
Must have
• Icons for phone, website, email, and Instagram instead of words. Specific colors used in my logo (171B2B, 421121, FFFFFF)
Nice to have
• Foil. Embossed. Feminine design.
Should not have
• Any colors other than those used in logo. See uploaded files.

```html
<!DOCTYPE html>
<html lang="en">
<head>
<meta charset="utf-8">
<title>Calm Brief Counsel – Business Card</title>
<link rel="stylesheet" href="https://fonts.googleapis.com/css2?family=Playfair+Display:wght@400&family=Sue+Ellen+Francisco&display=swap">
<style>
  :root {
    --navy: #171B2B;
    --wine: #421121;
    --white: #FFFFFF;
    --edge: #A9A9A9;
  }
  html, body {
    margin: 0;
    padding: 0;
    width: 1200px;
    height: 408px;
    overflow: hidden;
    background: var(--white);
  }
  .canvas {
    position: relative;
    width: 1200px;
    height: 408px;
  }
  .card {
    position: absolute;
    top: 34px;
    width: 558px;
    height: 330px;
    border-radius: 45px;
    box-sizing: border-box;
  }
  .card--front {
    left: 11px;
    background: var(--white);
    border: 1.5px solid var(--edge);
  }
  .card--back {
    left: 634px;
    background: var(--wine);
  }
  .brand-name {
    position: absolute;
    margin: 0;
    font-family: "Playfair Display", Georgia, serif;
    font-weight: 400;
    text-transform: uppercase;
    white-space: nowrap;
    transform: translate(-50%, -50%);
  }
  .card--front .brand-name {
    left: 279px;
    top: 168px;
    font-size: 30px;
    letter-spacing: 3px;
    color: var(--wine);
  }
  .card--back .brand-name {
    left: 122px;
    top: 168px;
    font-size: 15px;
    letter-spacing: 1.5px;
    color: var(--white);
  }
  .contact {
    position: absolute;
    left: 237px;
    top: 100px;
    margin: 0;
    padding: 0;
    list-style: none;
    font-family: "Sue Ellen Francisco", "Segoe Script", cursive;
    color: var(--white);
  }
  .contact__name {
    font-size: 21px;
    line-height: 30px;
    margin-bottom: 2px;
  }
  .contact__line {
    display: flex;
    align-items: center;
    gap: 7px;
    font-size: 18px;
    line-height: 23px;
  }
  .contact__icon {
    width: 12px;
    height: 12px;
    flex: none;
  }
</style>
</head>
<body>
  <main class="canvas">
    <section class="card card--front" aria-label="Card front">
      <h1 class="brand-name">Calm Brief Counsel</h1>
    </section>

    <section class="card card--back" aria-label="Card back">
      <p class="brand-name">Calm Brief Counsel</p>
      <ul class="contact">
        <li class="contact__name">Marissa Pendrell (life coach)</li>
        <li class="contact__line">518.677.3941</li>
        <li class="contact__line">
          <svg class="contact__icon" viewBox="0 0 12 12" aria-label="Email">
            <rect x="0.75" y="2.25" width="10.5" height="7.5" fill="none" stroke="#FFFFFF" stroke-width="1"/>
            <polyline points="0.75,2.5 6,6.5 11.25,2.5" fill="none" stroke="#FFFFFF" stroke-width="1"/>
          </svg>
          marissa@calmbriefcounsel.net
        </li>
        <li class="contact__line">
          <svg class="contact__icon" viewBox="0 0 12 12" aria-label="Website">
            <circle cx="6" cy="6" r="5.25" fill="none" stroke="#FFFFFF" stroke-width="1"/>
            <ellipse cx="6" cy="6" rx="2.3" ry="5.25" fill="none" stroke="#FFFFFF" stroke-width="1"/>
            <line x1="0.75" y1="6" x2="11.25" y2="6" stroke="#FFFFFF" stroke-width="1"/>
          </svg>
          calmbriefcounsel.net
        </li>
        <li class="contact__line">
          <svg class="contact__icon" viewBox="0 0 12 12" aria-label="Social profile">
            <rect x="1" y="1" width="10" height="10" rx="2" fill="none" stroke="#FFFFFF" stroke-width="1"/>
          </svg>
          @calmbriefcounsel
        </li>
      </ul>
    </section>
  </main>
</body>
</html>
```